Card for invoking rights with police

Our criminal defense law firm is seeking proposals for a design for our card intended for clients to carry with them in their car. Upon being pulled over, they would hand this card to the officer.
Text for the back of the card:
"For Law Enforcement:"
"I will comply with lawful orders but respectfully decline any test or other requests without my attorney. I wish to remain silent, do not consent to searches, and request to speak with my attorney now.
The back of the card should prominently feature the text and the firm logo should be secondary.
Front
Must prominently feature contact info: 503-555-0182. Do not include attorney name, email, phone from the example file. This is intended to be generic for the firm and not tied to an individual lawyer.
Included for design reference: current business card, firm logo.
We intend to use trenvo.com to produce the cards.
Updates
The back of the card should prominently display the text regarding invocation of rights. Please title it "For Law Enforcement".
Target Market(s)
People who have been stopped by police
Contact Information for Business Card
see project description
Look and feel

```html
<!DOCTYPE html>
<html lang="en">
<head>
<meta charset="utf-8">
<title>Harrow Law Firm – Cards</title>
<link href="https://fonts.googleapis.com/css2?family=Cinzel:wght@400;600&family=Montserrat:wght@400;500;600&display=swap" rel="stylesheet">
<style>
  :root{
    --navy:#0f3a5f;
    --navy-deep:#0b2e4d;
    --white:#ffffff;
    --paper:#fdfdfd;
    --faint:#eef1f4;
    --ink:#1d3550;
    --backdrop:#262626;
  }
  *{margin:0;padding:0;box-sizing:border-box}
  html,body{width:1200px;height:801px;overflow:hidden;background:var(--backdrop)}
  .stage{position:relative;width:1200px;height:801px}
  .card{position:absolute;top:246px;width:540px;height:309px;border-radius:22px;overflow:hidden}

  /* Front */
  .card--front{left:40px;background:var(--paper)}
  .front-mark{position:absolute;left:372px;top:118px;width:136px;height:136px;background:var(--faint)}
  .front-brand{position:absolute;right:34px;top:26px;color:var(--navy);font-family:"Cinzel",serif;font-weight:400}
  .front-brand .brand-name{font-size:30px;letter-spacing:10px;line-height:1;display:flex;align-items:center;gap:14px}
  .front-brand .brand-square{width:26px;height:26px;background:var(--navy)}
  .front-brand .brand-sub{font-size:11px;letter-spacing:3px;margin-top:8px;display:flex;align-items:center;gap:10px;justify-content:center;padding-left:40px}
  .front-brand .rule{display:inline-block;width:34px;height:1px;background:var(--navy)}
  .band{position:absolute;left:0;top:108px;width:320px;height:58px;background:var(--navy);color:var(--white);padding:10px 0 0 26px}
  .band .phone{font-family:"Cinzel",serif;font-weight:600;font-size:22px;letter-spacing:1.5px;line-height:1.1}
  .band .role{font-family:"Montserrat",sans-serif;font-size:10.5px;letter-spacing:1px;margin-top:3px}
  .address{position:absolute;left:44px;top:190px;font-family:"Montserrat",sans-serif;font-style:normal;font-size:11.5px;line-height:16px;color:var(--ink)}
  .contacts{position:absolute;left:44px;top:250px;list-style:none;font-family:"Montserrat",sans-serif;font-size:11.5px;line-height:17px;color:var(--ink)}
  .contacts li{display:flex;align-items:center;gap:8px}
  .contacts svg{width:11px;height:11px;fill:var(--navy)}

  /* Back */
  .card--back{left:620px;background:linear-gradient(135deg,var(--navy) 0%,var(--navy-deep) 100%);color:var(--white)}
  .back-brand{position:absolute;left:0;right:0;top:32px;display:flex;justify-content:center;align-items:center;gap:12px;font-family:"Cinzel",serif;font-weight:400}
  .back-brand .brand-square{width:30px;height:30px;background:var(--white)}
  .back-brand .brand-name{font-size:24px;letter-spacing:8px;line-height:1}
  .back-brand .brand-sub{font-size:9.5px;letter-spacing:3px;text-align:center;margin-top:5px;display:flex;align-items:center;gap:8px;justify-content:center}
  .back-brand .rule{display:inline-block;width:26px;height:1px;background:var(--white)}
  .rights-title{position:absolute;left:0;right:0;top:112px;text-align:center;font-family:"Cinzel",serif;font-weight:600;font-size:21px;letter-spacing:3px}
  .rights-title::after{content:"";display:block;width:60px;height:1px;background:var(--white);margin:10px auto 0}
  .rights{position:absolute;left:34px;right:34px;top:166px;text-align:center;font-family:"Montserrat",sans-serif;font-weight:500;font-size:15px;line-height:23px}
</style>
</head>
<body>
<main class="stage">
  <section class="card card--front" aria-label="Card front">
    <div class="front-mark" aria-hidden="true"></div>
    <div class="front-brand">
      <div class="brand-name"><span class="brand-square"></span>HARROW</div>
      <div class="brand-sub"><span class="rule"></span>LAW FIRM<span class="rule"></span></div>
    </div>
    <div class="band">
      <div class="phone">503-555-0182</div>
      <div class="role">CRIMINAL DEFENSE</div>
    </div>
    <address class="address">
      1280 Alder Lake Rd<br>Suite 210<br>Bellmont, WA 98100
    </address>
    <ul class="contacts">
      <li><svg viewBox="0 0 10 10"><path d="M2 1h2l1 2-1.2 1a5 5 0 0 0 2.2 2.2L7 5l2 1v2a1 1 0 0 1-1 1A7 7 0 0 1 1 2a1 1 0 0 1 1-1z"/></svg>503-555-0182</li>
      <li><svg viewBox="0 0 10 10"><circle cx="5" cy="5" r="4.5"/></svg>www.harrowlawfirm.com</li>
    </ul>
  </section>

  <section class="card card--back" aria-label="Card back">
    <div class="back-brand">
      <span class="brand-square"></span>
      <div>
        <div class="brand-name">HARROW</div>
        <div class="brand-sub"><span class="rule"></span>LAW FIRM<span class="rule"></span></div>
      </div>
    </div>
    <h2 class="rights-title">For Law Enforcement</h2>
    <p class="rights">I will comply with lawful orders but respectfully decline any test or other requests without my attorney. I wish to remain silent, do not consent to searches, and request to speak with my attorney now.</p>
  </section>
</main>
</body>
</html>
```